Non-Fiction Book Cover Series Concepts

I need front cover concepts for a non-fiction business book series. Just concepts at this stage to show to backers (full cover designs later).

The books are for leaders and business owners. A mature, sophisticated market, AND, bold and innovative.

The series needs to be extensible - the concepts need to be able to work across at least 40 books. I am happy with a colour theme, or contrasts, or icon theme, there is no limitation to the imagination.

The books need to look like they belong to a series and to also stand alone.

I prefer simple and bold.

Imagine the Heron trade series (https://www.heronbooks.example/series/tws/heron-trade-wisdom-series.html) - but I hate these designs (the colours don't work for me).

The imprint is MindfulVantagePress.example - the logo mark for the imprint is attached.

The books will be printed and ebooks - the printed version will be 5 inches by 8 inches form factor. They will be printed with a matt cover.

IF YOU WANT A BOOK TITLE TO TRY, use this:

Steady Momentum: Apply the R.A.V. Model to Inspire, Unlock and Sustain Talent

Thank you for your interest!

Target Market(s)

Business owners, leaders, entrepreneurs

Industry/Entity Type

Leadership

Font styles to use
Serif
Sans Serif

Requirements
Must have
• Extensible - the concept can work for many books and ALL books look part of the series
Nice to have
• I prefer simple, icons rather than photos
Should not have
• No photographic designs - icon, drawing

```html
<!DOCTYPE html>
<html lang="en">
<head>
<meta charset="utf-8">
<title>Broader Leadership – Book Cover</title>
<link rel="stylesheet" href="https://fonts.googleapis.com/css2?family=Archivo+Black&family=Jost:wght@200&family=Poppins:wght@300;700&display=swap">
<style>
  :root {
    --paper: #ffffff;
    --accent: #8383f4;
    --ink: #111111;
    --muted: #8c9a96;
    --dot-grey: #c1c9c6;
    --imprint: #1c2350;
  }
  html, body {
    margin: 0;
    padding: 0;
    overflow: hidden;
    background: var(--paper);
  }
  .cover {
    position: relative;
    width: 750px;
    height: 1200px;
    overflow: hidden;
    background: var(--paper);
  }
  .kicker, .subtitle {
    position: absolute;
    left: 70px;
    margin: 0;
    font-family: "Poppins", sans-serif;
    font-weight: 300;
    font-size: 18.5px;
    line-height: 25px;
    color: var(--muted);
  }
  .kicker { top: 66px; }
  .subtitle { top: 339px; font-size: 20px; }
  .rule {
    position: absolute;
    left: 70px;
    height: 2px;
    background: var(--accent);
  }
  .rule--top { top: 127px; width: 367px; }
  .rule--bottom { top: 321px; width: 576px; }
  .title {
    position: absolute;
    left: 66px;
    top: 140px;
    margin: 0;
  }
  .title__lead {
    display: flex;
    align-items: center;
    height: 90px;
    font-family: "Archivo Black", sans-serif;
    font-size: 101px;
    line-height: 1;
    color: var(--accent);
    letter-spacing: 1px;
  }
  .title__o {
    width: 128px;
    height: 73px;
    margin: 0 4px;
  }
  .title__main {
    display: block;
    margin-top: -4px;
    font-family: "Jost", sans-serif;
    font-weight: 200;
    font-size: 104px;
    line-height: 1;
    color: var(--ink);
    letter-spacing: -1px;
  }
  .network {
    position: absolute;
    left: 135px;
    top: 520px;
    width: 480px;
    height: 480px;
    border-radius: 50%;
    background: radial-gradient(circle at 50% 50%, var(--accent) 0 12px, var(--dot-grey) 13px 70%, #dde2e0 100%);
  }
  .imprint {
    position: absolute;
    left: 70px;
    top: 1128px;
    display: flex;
    align-items: center;
    gap: 8px;
    font-family: "Poppins", sans-serif;
    font-weight: 700;
    font-size: 17px;
    letter-spacing: 0.5px;
    color: var(--imprint);
  }
  .imprint__mark {
    width: 12px;
    height: 12px;
    border-radius: 50%;
    background: var(--imprint);
  }
</style>
</head>
<body>
<main class="cover">
  <p class="kicker">Lorem ipsum dolor sit amet,<br>consectetuer</p>
  <div class="rule rule--top"></div>
  <h1 class="title">
    <span class="title__lead">BR<svg class="title__o" viewBox="0 0 128 73" aria-hidden="true"><rect x="0" y="0" width="128" height="73" rx="32" fill="var(--accent)"/><circle cx="64" cy="36.5" r="13" fill="var(--paper)"/></svg>ADER</span>
    <span class="title__main">LEADERSHIP</span>
  </h1>
  <div class="rule rule--bottom"></div>
  <p class="subtitle">Lorem ipsum dolor sit amet, consectetuer<br>Lorem ipsum</p>
  <div class="network" role="img" aria-label="Radiating pattern of grey dots around a single accent-coloured central dot"></div>
  <div class="imprint"><span class="imprint__mark"></span>MINDFUL VANTAGE PRESS</div>
</main>
</body>
</html>
```